Build Website for Playful Brand that helps content creators build businesses

Please help me create a website for my company that helps content creators build businesses around their audience. I have attached a design and vibe that I am going for at plumfinch.io.

Open for changes, but I want to keep the colour I currently have (a light teal). Ultimately the brand is playful but should come off as a very modern elevated brand.

I am looking for a few pages including

1. Home (with clear CTA button)
A section where I can input what the company does, and some brands that we have launched

2. About Me
A simple page, that has preferably able to put a circular image of myself and then give a quick background about the company

3. Blog (can you include how blog posts will appear and it should sit nicely in the page)
This ideally is a section that will be able to link to another software so my blogs automatically flow into here or posts. But otherwise it should have sections of blocks where creators can see about topics that I post about

4. Contact (this should include a form that will allow users to contact me)
Finally a contact page where it links my socials, similar what is there, but ideally there is a form they can fill out which I can link to my inbox as well. This should be a simple page as well

Create a multi page website, including a page that will link or can link blog post

Similar to this vibe and logo - https://plumfinch.io/

Target Market(s)

Content Creators

Coding

Coded - Design and coding required

Number of Pages Required

4 page

Requirements
Must have
• Home, Contact Me (Including a place to submit an enquiry and form), Blog Post Page As well

```html
<!DOCTYPE html>
<html lang="en">
<head>
<meta charset="utf-8">
<title>Plum Finch — Building Businesses</title>
<link rel="stylesheet" href="https://fonts.googleapis.com/css2?family=Outfit:wght@300;400;500;600;700&display=swap">
<style>
:root{
  --bg:#e3faf7;
  --ink:#344a4f;
  --ink-soft:#4b6166;
  --line:#9fc9c7;
  --mint:#bfece6;
  --card:#f8fbfb;
  --white:#ffffff;
  --chip:#c8efe9;
}
*{box-sizing:border-box;margin:0;padding:0}
html,body{width:1200px;height:3084px;overflow:hidden}
body{background:var(--bg);font-family:"Outfit",sans-serif;color:var(--ink);position:relative}
.abs{position:absolute}
a{color:inherit;text-decoration:none}

/* header */
.brand{display:flex;flex-direction:column;align-items:center;gap:8px}
.brand-dot{width:44px;height:44px;border-radius:50%;background:var(--mint);border:2px solid var(--line)}
.brand-name{font-weight:400;letter-spacing:3px;font-size:22px;color:var(--ink)}
.site-brand{left:114px;top:18px;width:160px}
.nav{top:30px;left:518px;display:flex;align-items:center;font-size:15px;letter-spacing:.5px}
.nav a{padding:0 0 6px}
.nav .active{border-bottom:2px solid var(--ink)}
.nav .sep{margin:0 42px 6px;color:var(--ink-soft)}
.btn{display:inline-flex;align-items:center;justify-content:center;background:var(--ink);color:var(--white);border-radius:30px;font-weight:600;letter-spacing:.6px}
.nav-cta{left:926px;top:22px;width:147px;height:40px;font-size:14px;font-weight:500}

/* hero */
.hero-line{left:0;top:264px;width:96px;height:1px;background:var(--ink-soft)}
.hero-line::after{content:"";position:absolute;right:-3px;top:-4px;width:9px;height:9px;border-radius:50%;background:var(--ink-soft)}
.hero-title{left:114px;top:216px;font-size:72px;font-weight:700;line-height:68px;letter-spacing:1px}
.hero-sub{left:120px;top:370px;font-size:23px;font-weight:400;line-height:32px;color:var(--ink-soft)}
.hero-cta{left:120px;top:448px;width:169px;height:46px;font-size:15px}
.hero-art{left:570px;top:105px;width:630px;height:470px;background:radial-gradient(ellipse at 50% 50%,#d0eeee 0%,#dcf4f2 45%,var(--bg) 75%)}

/* brands */
.brands{left:103px;top:615px;width:1005px;height:221px;background:var(--card);border-radius:26px 26px 60px 26px;box-shadow:0 10px 30px rgba(52,74,79,.06)}
.brands h2{position:absolute;top:42px;width:100%;text-align:center;font-size:21px;font-weight:600;letter-spacing:.5px}
.brand-row{position:absolute;top:108px;left:70px;right:60px;display:flex;justify-content:space-between;align-items:center}
.partner{font-size:22px;font-weight:500;color:var(--ink);display:flex;align-items:center;gap:8px}
.partner .mk{width:14px;height:14px;background:var(--ink)}
.partner .mc{width:14px;height:14px;border-radius:50%;background:var(--ink)}

/* about */
.about-ring{left:108px;top:920px;width:470px;height:470px;border-radius:50%;border:2px solid #c6dfde}
.about-ring2{left:126px;top:938px;width:434px;height:434px;border-radius:50%;border:1px solid #c6dfde}
.about-photo{left:139px;top:950px;width:408px;height:408px;border-radius:50%;background:linear-gradient(180deg,#d6f4f1 0%,#c9ece9 55%,#b9d4e6 100%)}
.ring-dot{width:7px;height:7px;border-radius:50%;background:var(--ink)}
.eyebrow{font-size:15px;letter-spacing:3px;color:var(--ink-soft);font-weight:400}
.about-eyebrow{left:647px;top:955px}
.h-section{font-weight:700;display:flex;align-items:center;gap:12px}
.h-dot{width:34px;height:34px;border-radius:50%;background:var(--mint);border:2px solid var(--line)}
.about-title{left:647px;top:976px;font-size:58px}
.about-line{left:1057px;top:1002px;width:143px;height:1px;background:var(--ink-soft)}
.about-line::before{content:"";position:absolute;left:-4px;top:-4px;width:9px;height:9px;border-radius:50%;background:var(--ink-soft)}
.about-copy{left:651px;top:1060px;width:446px;font-size:18.5px;letter-spacing:.35px;line-height:23px;color:var(--ink)}
.about-copy p+p{margin-top:23px}
.about-cta{left:652px;top:1309px;width:175px;height:48px;font-size:15px}

/* blogs */
.blogs-eyebrow{left:110px;top:1518px}
.blogs-title{left:110px;top:1540px;font-size:48px}
.blogs-line{left:0;top:1571px;width:74px;height:1px;background:var(--ink-soft)}
.blogs-line::after{content:"";position:absolute;right:-3px;top:-4px;width:9px;height:9px;border-radius:50%;background:var(--ink-soft)}
.post-feature{left:107px;top:1662px;width:505px;height:401px;background:linear-gradient(180deg,#8d9797 0%,#6f7d7c 55%,#3d4f50 100%)}
.post-feature .date{position:absolute;left:35px;top:290px}
.post-feature h3{position:absolute;left:35px;top:318px;width:430px;color:var(--white);font-size:21px;font-weight:600;line-height:27px}
.date{display:inline-flex;align-items:center;gap:5px;background:var(--chip);color:var(--ink);font-size:12px;font-weight:500;padding:3px 9px}
.date svg{width:11px;height:11px}
.post{left:625px;width:466px;height:190px;background:var(--white);border:1px solid #a9b8b8;display:flex}
.post .thumb{width:223px;height:100%;background:linear-gradient(135deg,#c9cdca,#7e8b8e)}
.post .body{padding:24px 16px 0 26px}
.post h4{font-size:14.5px;font-weight:600;margin:14px 0 8px}
.post p{font-size:11.5px;line-height:17px;color:var(--ink-soft);width:196px}
.post .more{display:inline-block;margin-top:9px;border:1px solid var(--ink);font-size:9px;font-weight:600;padding:5px 16px;letter-spacing:.5px}
.post-a{top:1663px}
.post-b{top:1869px}

/* band */
.wave-band{left:0;top:2095px;width:1200px;height:190px;background:linear-gradient(180deg,var(--bg) 0%,#d4eeec 50%,var(--bg) 100%)}

/* contact */
.contact-stem{left:619px;top:2300px;width:1px;height:60px;background:var(--ink-soft)}
.contact{left:170px;top:2340px;width:919px;height:517px;background:#344a4f;border-radius:4px}
.contact .h-dot{position:absolute;left:436px;top:45px;width:46px;height:46px;background:var(--mint)}
.contact h2{position:absolute;top:94px;width:100%;text-align:center;color:var(--white);font-size:38px;font-weight:700;letter-spacing:.5px}
.field{position:absolute;background:var(--white);font-size:14px;color:var(--ink);padding:14px 22px;font-family:inherit}
.f1{left:82px;top:163px;width:360px;height:50px}
.f2{left:455px;top:163px;width:362px;height:50px}
.f3{left:82px;top:226px;width:360px;height:50px}
.f4{left:455px;top:226px;width:362px;height:50px}
.f5{left:82px;top:290px;width:735px;height:107px}
.send{position:absolute;left:348px;top:417px;width:208px;height:51px;border:1.5px solid #c9dcdc;border-radius:30px;color:var(--white);font-size:17px;font-weight:600;display:flex;align-items:center;justify-content:center}

/* footer */
.foot-rule{height:1px;background:#b7cfcf}
.foot-nav{font-size:14px;font-weight:600;letter-spacing:2.5px;display:flex;align-items:center}
.foot-nav .b{width:7px;height:7px;border-radius:50%;background:var(--ink);margin:0 45px}
.foot-brand{left:533px;top:2895px;width:160px}
.foot-brand .brand-dot{width:62px;height:62px}
.copyright{left:206px;top:3031px;font-size:13px}
.follow{left:876px;top:3026px;font-size:13px;display:flex;align-items:center;gap:14px}
.social{font-weight:600;font-size:13px;display:flex;align-items:center;gap:5px}
.social i{width:10px;height:10px;background:var(--ink);display:inline-block}
</style>
</head>
<body>

<!-- header -->
<a class="abs brand site-brand" href="https://plumfinch.io/"><span class="brand-dot"></span><span class="brand-name">PLUM FINCH</span></a>
<nav class="abs nav">
  <a class="active" href="#">HOME</a><span class="sep">|</span>
  <a href="#">ABOUT ME</a><span class="sep">|</span>
  <a href="#">BLOG</a>
</nav>
<a class="abs btn nav-cta" href="#contact">CONTACT ME</a>

<!-- hero -->
<div class="abs hero-art" role="img" aria-label="Illustration of a brand location pin above an isometric analytics dashboard"></div>
<span class="abs hero-line"></span>
<h1 class="abs hero-title">BUILDING<br>BUSINESSES</h1>
<p class="abs hero-sub">Helping Content Creators<br>Build Their Own Brand</p>
<a class="abs btn hero-cta" href="#">LEARN MORE</a>

<!-- brands -->
<section class="abs brands">
  <h2>SUCCESSFUL BRANDS</h2>
  <div class="brand-row">
    <span class="partner"><i class="mk"></i>HALVORSEN</span>
    <span class="partner">Northgate</span>
    <span class="partner">WELDRA</span>
    <span class="partner"><i class="mc"></i>Kestrel Estates</span>
    <span class="partner" style="letter-spacing:5px;font-size:15px">MARLOWE DUNN</span>
  </div>
</section>

<!-- about -->
<span class="abs about-ring"></span>
<span class="abs about-ring2"></span>
<div class="abs about-photo" role="img" aria-label="Circular portrait photo of the founder"></div>
<span class="abs ring-dot" style="left:204px;top:983px"></span>
<span class="abs ring-dot" style="left:467px;top:1346px"></span>
<p class="abs eyebrow about-eyebrow">WHO WE ARE</p>
<h2 class="abs h-section about-title">ABOUT ME <span class="h-dot"></span></h2>
<span class="abs about-line"></span>
<div class="abs about-copy">
  <p>Lorem ipsum dolor sit amet, consectetur adipiscing elit, sed do eiusmod tempor incididunt ut labore et dolore magna aliqua. Ut enim ad minim veniam, quis nostrud exercitation ullamco laboris nisi ut</p>
  <p>Aliquip ex ea commodo consequat. Duis aute irure dolor in reprehenderit in voluptate velit esse cillum dolore eu fugiat nulla pariatur. Excepteur sint occaecat cupidatat non proident, sunt in culpa</p>
</div>
<a class="abs btn about-cta" href="#">LEARN MORE</a>

<!-- blogs -->
<p class="abs eyebrow blogs-eyebrow">BLOGS &amp; RESOURCES</p>
<h2 class="abs h-section blogs-title">LATEST BLOGS <span class="h-dot"></span></h2>
<span class="abs blogs-line"></span>

<article class="abs post-feature" role="img" aria-label="Photo of a team working together at computers">
  <span class="date"><svg viewBox="0 0 12 12"><circle cx="6" cy="6" r="5" fill="none" stroke="currentColor"/><path d="M6 3v3l2 1" fill="none" stroke="currentColor"/></svg>19 JAN 2024</span>
  <h3>Lorem ipsum dolor sit amet consec tetur adipiscing elit sed do</h3>
</article>

<article class="abs post post-a">
  <div class="thumb" role="img" aria-label="Photo of colleagues reviewing work at a desk"></div>
  <div class="body">
    <span class="date"><svg viewBox="0 0 12 12"><circle cx="6" cy="6" r="5" fill="none" stroke="currentColor"/><path d="M6 3v3l2 1" fill="none" stroke="currentColor"/></svg>19 JAN 2024</span>
    <h4>Lorem ipsum dolor sit</h4>
    <p>Lorem ipsum dolor sit amet consectetur adipiscing elit sed do eiusmod tempor incididunt ut labor</p>
    <a class="more" href="#">LEARN MORE</a>
  </div>
</article>

<article class="abs post post-b">
  <div class="thumb" role="img" aria-label="Photo of a smiling team gathered around a laptop"></div>
  <div class="body">
    <span class="date"><svg viewBox="0 0 12 12"><circle cx="6" cy="6" r="5" fill="none" stroke="currentColor"/><path d="M6 3v3l2 1" fill="none" stroke="currentColor"/></svg>19 JAN 2024</span>
    <h4>Lorem ipsum dolor sit</h4>
    <p>Lorem ipsum dolor sit amet consectetur adipiscing elit sed do eiusmod tempor incididunt ut labor</p>
    <a class="more" href="#">LEARN MORE</a>
  </div>
</article>

<div class="abs wave-band" role="img" aria-label="Soft decorative dotted wave pattern"></div>

<!-- contact -->
<span class="abs contact-stem"></span>
<section class="abs contact" id="contact">
  <span class="h-dot"></span>
  <h2>CONTACT ME</h2>
  <div class="field f1">First Name*</div>
  <div class="field f2">Last Name*</div>
  <div class="field f3">Email address*</div>
  <div class="field f4">Phone*</div>
  <div class="field f5">Leave Message</div>
  <a class="send" href="#">Send Message</a>
</section>

<!-- footer -->
<span class="abs foot-rule" style="left:148px;top:2927px;width:370px"></span>
<span class="abs foot-rule" style="left:708px;top:2927px;width:370px"></span>
<span class="abs foot-rule" style="left:148px;top:2990px;width:370px"></span>
<span class="abs foot-rule" style="left:708px;top:2990px;width:370px"></span>
<nav class="abs foot-nav" style="left:212px;top:2950px"><a href="#">HOME</a><span class="b"></span><a href="#">ABOUT US</a></nav>
<nav class="abs foot-nav" style="left:761px;top:2950px"><a href="#">BLOGS</a><span class="b"></span><a href="#contact">CONTACT US</a></nav>
<a class="abs brand foot-brand" href="https://plumfinch.io/"><span class="brand-dot"></span><span class="brand-name">PLUM FINCH</span></a>
<p class="abs copyright">Copyright © 2024 Plum Finch. All Right Reserved</p>
<div class="abs follow">Follow Us On <a class="social" href="#"><i></i>Snapgram</a><a class="social" href="#"><i></i>Worknet</a></div>

</body>
</html>
```